Brightmoor Partners Branding Revamp

We are a consulting company, looking for a way to display and promote our brand. We have 2 sides to the business- Brightmoor (financial) and Partners (cyber security). The financial side products relate to business necessities: card processing, website design/hosting/maintenance, VoIP phone systems. The cyber security side promotes a bundled package of 4 solutions: network vulnerability scan, dark web scan, anti-ransomeware/malware software, and image-level backups. We want people to understand that partnering with Brightmoor Partners gives them “Steady Ground Ahead” (tagline). Current badge and logos uploaded.

Target Market(s)

Small businesses

Contact Information for Business Card

Lena Marwick, Vice President, lena@brightmoorpartners.example, 555-806-1937, www.brightmoorpartners.example

Requirements
Nice to have
• I do prefer the darker background for front and back

```html
<!DOCTYPE html>
<html lang="en">
<head>
<meta charset="utf-8">
<title>Brightmoor Partners — Business Card</title>
<link rel="stylesheet" href="https://fonts.googleapis.com/css2?family=Source+Sans+3:wght@400;600;700&display=swap">
<style>
  :root {
    --page-bg: #e6e6e6;
    --card-bg: #242424;
    --pattern-light: #6e6e6e;
    --pattern-mid: #2c2c2c;
    --pattern-dark: #050505;
    --accent-red: #e21d24;
    --text-white: #ffffff;
    --divider-grey: #8a8a8a;
  }
  * { margin: 0; padding: 0; box-sizing: border-box; }
  html, body { width: 1200px; height: 960px; overflow: hidden; }
  body {
    background: var(--page-bg);
    font-family: "Source Sans 3", "Source Sans Pro", sans-serif;
    position: relative;
  }
  .card {
    position: absolute;
    left: 299px;
    width: 600px;
    height: 341px;
  }
  .card-front {
    top: 119px;
    background: linear-gradient(115deg, var(--pattern-light) 0%, var(--pattern-mid) 45%, var(--pattern-dark) 100%);
    display: flex;
    align-items: center;
    justify-content: center;
  }
  .front-name {
    color: var(--text-white);
    font-weight: 600;
    font-size: 26px;
    letter-spacing: 4px;
    text-transform: uppercase;
  }
  .card-back {
    top: 514px;
    background: var(--card-bg);
    color: var(--text-white);
  }
  .brand {
    position: absolute;
    left: 40px;
    top: 100px;
    width: 230px;
    text-align: center;
  }
  .brand-mark {
    display: block;
    width: 46px;
    height: 46px;
    margin: 0 auto 16px;
    background: var(--accent-red);
  }
  .brand-name {
    font-weight: 600;
    font-size: 24px;
    letter-spacing: 5px;
    line-height: 1.2;
    text-transform: uppercase;
    color: var(--text-white);
  }
  .divider {
    position: absolute;
    left: 298px;
    width: 1px;
  }
  .divider-red { top: 102px; height: 46px; background: var(--accent-red); }
  .divider-grey { top: 156px; height: 82px; background: var(--divider-grey); }
  .person {
    position: absolute;
    left: 331px;
    top: 100px;
  }
  .person-name {
    color: var(--accent-red);
    font-weight: 700;
    font-size: 20px;
    letter-spacing: 0.3px;
    line-height: 26px;
  }
  .person-title {
    font-size: 15px;
    line-height: 20px;
  }
  .contact {
    position: absolute;
    left: 331px;
    top: 176px;
    list-style: none;
    font-size: 15px;
    line-height: 20px;
  }
  .contact li { display: flex; align-items: center; gap: 5px; }
  .contact svg { width: 13px; height: 13px; flex: none; }
  .tagline {
    position: absolute;
    left: 0;
    right: 0;
    top: 294px;
    text-align: center;
    font-weight: 700;
    font-size: 15px;
    text-transform: uppercase;
  }
  .tagline em { font-style: normal; color: var(--accent-red); }
</style>
</head>
<body>
  <section class="card card-front" role="img" aria-label="Dark glossy repeating hexagon pattern with the company name at the centre">
    <span class="front-name">Brightmoor Partners</span>
  </section>

  <section class="card card-back">
    <div class="brand">
      <span class="brand-mark"></span>
      <div class="brand-name">Brightmoor<br>Partners</div>
    </div>

    <span class="divider divider-red"></span>
    <span class="divider divider-grey"></span>

    <div class="person">
      <div class="person-name">LENA MARWICK</div>
      <div class="person-title">Vice President</div>
    </div>

    <ul class="contact">
      <li>
        <svg viewBox="0 0 16 16" fill="none" stroke="#e21d24" stroke-width="1.6"><path d="M4 1.5l2.5 3-1.5 2a8 8 0 0 0 4.5 4.5l2-1.5 3 2.5-1.5 2.5C7 14.5 1.5 9 1.5 3z"/></svg>
        555-806-1937
      </li>
      <li>
        <svg viewBox="0 0 16 16" fill="none" stroke="#e21d24" stroke-width="1.6"><rect x="1" y="3" width="14" height="10"/><path d="M1 3l7 6 7-6"/></svg>
        lena@brightmoorpartners.example
      </li>
      <li>
        <svg viewBox="0 0 16 16" fill="none" stroke="#e21d24" stroke-width="1.4"><circle cx="8" cy="8" r="6.5"/><ellipse cx="8" cy="8" rx="3" ry="6.5"/><path d="M1.5 8h13"/></svg>
        www.brightmoorpartners.example
      </li>
    </ul>

    <p class="tagline">Steady Ground <em>Ahead</em></p>
  </section>
</body>
</html>
```